We are a Yacht Charter Broker servicing VIP clients on booking sailing catamarans and motor yacht...

We are looking for a wildly creative website to attract high net worth clients to work with us in booking their dream yacht vacation. A site that you think is 5 years ahead of its time. Sexy, modern and unique. Our company name is BRELLAVON. Our colors are navy blue and silver.
BLUE:
RGBB 0/44/92
CMYC 100/86/36/31
SILVER:
RGB 152/163/173
CMYK 43/29/25/0

HEX 98a3ad

Target Market(s)

High net worth people in need of white glove brokerage serving in finding and booking their dream yacht for a vacation of a lifetime.

Coding

Coded - Design and coding required

Number of Pages Required

1 page

Requirements
Must have
• Mobile friendly.
• Wildly creative and different. A website that we would expect to see 5 years from now.
• Pictures of yachts and or people on yachts. Palm tree landscapes.
• pictures of high end food related to the VIP yacht experience.
Nice to have
• Anything you feel would sell the yacht charter experience.
Should not have
• Nothing comes to mind.

```html
<!DOCTYPE html>
<html lang="en">
<head>
<meta charset="utf-8">
<title>Brellavon — Yacht Charter Brokerage</title>
<link href="https://fonts.googleapis.com/css2?family=Cormorant+Garamond:wght@400;500&family=Lato:wght@300;400;700&display=swap" rel="stylesheet">
<style>
:root{
  --navy:#0d2b55;
  --navy-deep:#0a2347;
  --silver:#98a3ad;
  --panel:#f2f2f2;
  --text:#333;
  --muted:#8a8f96;
  --white:#fff;
  --line:#d9dce0;
}
*{box-sizing:border-box;margin:0;padding:0}
html,body{width:1200px;height:4489px;overflow:hidden}
body{position:relative;background:var(--white);font-family:'Lato',sans-serif;color:var(--text)}
.abs{position:absolute}
.serif{font-family:'Cormorant Garamond',serif;font-variant-numeric:lining-nums}
.btn{position:absolute;display:flex;align-items:center;justify-content:center;border-radius:20px;font-size:14px;font-family:'Lato',sans-serif}
.btn-navy{background:var(--navy);color:var(--white)}
.btn-light{background:#e6e6e6;color:var(--navy)}
.btn-white{background:var(--white);color:var(--navy)}
.rule{position:absolute;height:2px;background:var(--navy)}
.section-title{position:absolute;left:0;width:1200px;text-align:center;font-family:'Cormorant Garamond',serif;font-size:30px;letter-spacing:1px;color:#222;font-weight:400}
.body-copy{font-size:13px;line-height:19px;color:var(--muted);text-align:center}
.photo{position:absolute}

/* header */
.site-header{position:absolute;left:0;top:0;width:1200px;height:84px;background:var(--white)}
.brand{position:absolute;left:114px;top:26px;font-family:'Cormorant Garamond',serif;font-size:26px;letter-spacing:4px;color:var(--navy)}
.main-nav{position:absolute;left:578px;top:34px;display:flex;gap:24px;font-size:14px;color:#333}
.header-cta{left:964px;top:27px;width:124px;height:34px}

/* hero */
.hero{left:0;top:84px;width:1200px;height:664px;background:linear-gradient(180deg,#4c86c4 0%,#9cc3e4 45%,#3fa0b8 62%,#1f7d93 100%)}
.hero-title{position:absolute;left:114px;top:292px;font-family:'Cormorant Garamond',serif;font-size:40px;font-weight:400;letter-spacing:2px;color:var(--white)}

/* features */
.feature{position:absolute;top:688px;width:340px;text-align:center}
.feature-badge{width:168px;height:168px;margin:0 auto;border-radius:50%;background:var(--navy);border:6px solid var(--white);display:flex;align-items:center;justify-content:center}
.feature-name{margin-top:38px;font-family:'Cormorant Garamond',serif;font-variant-numeric:lining-nums;font-size:21px;letter-spacing:1px;color:#333}
.feature-rule{width:70px;height:2px;background:var(--navy);margin:26px auto 24px}

/* split rows */
.split-panel{position:absolute;background:var(--panel)}
.split-title{position:absolute;width:600px;text-align:center;font-family:'Cormorant Garamond',serif;font-size:27px;font-weight:400;letter-spacing:1px;color:#222}
.split-copy{position:absolute;width:400px}

/* destinations */
.destination{position:absolute;top:2229px;width:246px;height:246px;border-radius:50%}
.chevron{position:absolute;top:2330px}

/* testimonial */
.testimonials{left:0;top:3029px;width:1200px;height:401px;background:linear-gradient(90deg,#1b3c6a 0%,#2d5686 50%,#1b3c6a 100%)}

/* booking */
.booking-info{left:159px;top:3523px;width:440px;height:518px;background:var(--panel)}
.booking-form{left:599px;top:3523px;width:443px;height:518px;background:var(--navy)}
.field-label{position:absolute;font-size:13px;color:var(--white)}
.field{position:absolute;background:var(--white);height:34px;font-size:12px;color:#444;display:flex;align-items:center;padding-left:10px}
.field .caret{position:absolute;right:10px;top:14px}

/* footer */
.site-footer{left:0;top:4139px;width:1200px;height:291px;background:var(--navy)}
.footer-head{position:absolute;top:4199px;font-family:'Cormorant Garamond',serif;font-size:18px;font-weight:400;letter-spacing:1px;color:var(--white)}
.footer-rule{position:absolute;top:4239px;width:46px;height:1px;background:var(--white)}
.footer-text{position:absolute;font-size:13px;line-height:18px;color:var(--white)}
.footer-list{position:absolute;top:4268px;list-style:none;font-size:13px;color:var(--white);line-height:27px}
.footer-list li::before{content:"•";margin-right:10px}
.contact-list{position:absolute;left:883px;top:4262px;list-style:none;font-size:13px;color:var(--white);line-height:27px}
.contact-list li{display:flex;align-items:center;gap:12px}
.bottom-bar{left:0;top:4430px;width:1200px;height:59px;background:var(--white);font-size:12px;color:#333}
</style>
</head>
<body>

<header class="site-header">
  <div class="brand">BRELLAVON</div>
  <nav class="main-nav"><span>Charter a yacht</span><span>Locations</span><span>About us</span><span>Contact us</span></nav>
  <div class="btn btn-navy header-cta">Book a Yacht</div>
</header>

<section class="photo hero" role="img" aria-label="Guests standing on a white motor yacht on turquoise water beside a green island under a blue sky">
</section>
<h1 class="hero-title">YACHT CHARTER BROKRAGE</h1>
<div class="btn btn-light" style="left:114px;top:366px;width:140px;height:40px">Read More</div>
<div class="btn btn-navy" style="left:266px;top:366px;width:140px;height:40px">Contact us</div>

<div class="feature" style="left:90px">
  <div class="feature-badge">
    <svg width="52" height="40" viewBox="0 0 52 40" fill="none" stroke="#fff" stroke-width="3"><path d="M4 4v32M4 28h44v8M4 20h44v8"/><circle cx="14" cy="15" r="4" fill="#fff"/><path d="M22 20v-8h20a6 6 0 0 1 6 6v2"/></svg>
  </div>
  <div class="feature-name">LUXURY CABINS</div>
  <div class="feature-rule"></div>
  <p class="body-copy">Lorem Ipsum is simply dummy<br>text of the printing and<br>typesetting industry.</p>
</div>
<div class="feature" style="left:430px">
  <div class="feature-badge">
    <svg width="46" height="44" viewBox="0 0 24 23"><path fill="#fff" d="M12 0l3.1 7.6 8.1.6-6.2 5.2 2 7.9L12 17l-7 4.3 2-7.9L.8 8.2l8.1-.6z"/></svg>
  </div>
  <div class="feature-name">PROFESSIONAL CREW</div>
  <div class="feature-rule"></div>
  <p class="body-copy">Lorem Ipsum is simply dummy<br>text of the printing and<br>typesetting industry.</p>
</div>
<div class="feature" style="left:767px">
  <div class="feature-badge">
    <svg width="62" height="40" viewBox="0 0 62 40" fill="none" stroke="#fff" stroke-width="3"><path d="M4 26h54l-8 8H12z"/><path d="M14 26l6-10h22l8 10"/><path d="M22 16l4-8h12"/><path d="M4 38q6-4 12 0t12 0 12 0 12 0"/></svg>
  </div>
  <div class="feature-name">100 OF YACHTS</div>
  <div class="feature-rule"></div>
  <p class="body-copy">Lorem Ipsum is simply dummy<br>text of the printing and<br>typesetting industry.</p>
</div>

<div class="abs" style="left:0;top:1083px;width:1200px;height:1px;background:var(--line)"></div>

<h2 class="section-title" style="top:1150px">OUR YACHTS</h2>
<div class="rule" style="left:565px;top:1209px;width:70px"></div>

<div class="split-panel" style="left:0;top:1287px;width:600px;height:380px"></div>
<h3 class="split-title" style="left:0;top:1375px">MOTOR YACHTS</h3>
<div class="rule" style="left:265px;top:1425px;width:70px"></div>
<p class="body-copy split-copy" style="left:100px;top:1470px">Lorem Ipsum is simply dummy text of the printing and typesetting industry. Lorem Ipsum has been the industry's standard dummy text ever since the 1500s, when an unknown printer took a galley of type and scrambled it to make a type specimen book.</p>
<div class="photo" style="left:600px;top:1287px;width:600px;height:380px;background:linear-gradient(160deg,#2a5f8f 0%,#3d7aa6 50%,#6f9cc0 100%)" role="img" aria-label="White motor yacht speeding across deep blue water"></div>

<div class="photo" style="left:0;top:1667px;width:600px;height:383px;background:radial-gradient(circle at 40% 50%,#1d6aa8 0%,#0f4c84 60%,#0b3a68 100%)" role="img" aria-label="Aerial view of a sailing catamaran on deep blue sea"></div>
<div class="split-panel" style="left:600px;top:1667px;width:600px;height:383px"></div>
<h3 class="split-title" style="left:600px;top:1758px">SAILING CATAMARANS</h3>
<div class="rule" style="left:865px;top:1808px;width:70px"></div>
<p class="body-copy split-copy" style="left:700px;top:1853px">Lorem Ipsum is simply dummy text of the printing and typesetting industry. Lorem Ipsum has been the industry's standard dummy text ever since the 1500s, when an unknown printer took a galley of type and scrambled it to make a type specimen book.</p>

<h2 class="section-title" style="top:2105px">DESTINATIONS</h2>
<div class="rule" style="left:565px;top:2167px;width:70px"></div>
<svg class="chevron" style="left:80px" width="20" height="44" viewBox="0 0 20 44"><path d="M16 2L4 22l12 20" fill="none" stroke="#222" stroke-width="3"/></svg>
<div class="destination" style="left:158px;background:linear-gradient(180deg,#4fa6dc 0%,#5fb0a8 50%,#c9b28a 100%)" role="img" aria-label="Tropical beach bay with limestone cliffs"></div>
<div class="destination" style="left:478px;background:linear-gradient(180deg,#7fb6e0 0%,#5f8e5a 45%,#c9573d 75%,#2d5c7a 100%)" role="img" aria-label="Colourful harbour houses beneath green mountains"></div>
<div class="destination" style="left:796px;background:linear-gradient(180deg,#5d9fd8 0%,#7fa45c 50%,#b9a37a 80%,#3b7a5e 100%)" role="img" aria-label="Old stone bridge over a green river town"></div>
<svg class="chevron" style="left:1100px" width="20" height="44" viewBox="0 0 20 44"><path d="M4 2l12 20L4 42" fill="none" stroke="#222" stroke-width="3"/></svg>
<div class="btn btn-navy" style="left:518px;top:2549px;width:164px;height:38px">All Destinations</div>

<div class="split-panel" style="left:0;top:2664px;width:608px;height:359px"></div>
<h2 class="split-title" style="left:0;top:2728px;font-size:30px">ABOUT US</h2>
<div class="rule" style="left:268px;top:2793px;width:70px"></div>
<p class="body-copy split-copy" style="left:104px;top:2823px">Lorem Ipsum is simply dummy text of the printing and typesetting industry. Lorem Ipsum has been the industry's standard dummy text ever since the 1500s, when an unknown printer took a galley of type and scrambled it to make a type specimen book.</p>
<div class="photo" style="left:620px;top:2664px;width:580px;height:359px;background:linear-gradient(150deg,#1f5384 0%,#3a78a8 55%,#8fb3cf 100%)" role="img" aria-label="Motor yacht cutting a white wake across the sea"></div>

<section class="photo testimonials" role="img" aria-label="Smiling guests in sunglasses aboard a yacht, under a navy overlay"></section>
<h2 class="section-title" style="top:3066px;color:var(--white)">WHAT CLIENTS SAY</h2>
<svg class="abs" style="left:80px;top:3210px" width="20" height="44" viewBox="0 0 20 44"><path d="M16 2L4 22l12 20" fill="none" stroke="#fff" stroke-width="3"/></svg>
<svg class="abs" style="left:1082px;top:3210px" width="20" height="44" viewBox="0 0 20 44"><path d="M4 2l12 20L4 42" fill="none" stroke="#fff" stroke-width="3"/></svg>
<div class="abs serif" style="left:0;width:1200px;top:3150px;text-align:center;color:var(--white);font-size:54px;line-height:54px">&#8221;</div>
<p class="abs" style="left:270px;top:3212px;width:660px;font-size:13px;line-height:18px;color:var(--white);text-align:center">Lorem Ipsum is simply dummy text of the printing and typesetting industry. Lorem Ipsum has been the industry's standard dummy text ever since the 1500s, when an unknown printer took a galley of type and scrambled it to make a type specimen book.</p>
<div class="abs" style="left:0;width:1200px;top:3278px;text-align:center;color:var(--white);font-size:12px;line-height:16px">MARCUS HALE<br>(Client)</div>
<div class="abs" style="left:436px;top:3328px;width:328px;height:1px;background:var(--white)"></div>
<div class="btn btn-white" style="left:518px;top:3345px;width:164px;height:38px">All Testimonials</div>

<section class="abs booking-info">
  <h2 class="serif" style="position:absolute;left:0;width:440px;top:78px;text-align:center;font-size:28px;color:#222;font-weight:400">Book a yacht</h2>
  <div class="rule" style="left:185px;top:133px;width:70px"></div>
  <div style="position:absolute;left:40px;top:165px;width:340px;font-size:13px;line-height:18px;color:var(--muted)">
    <p>Lorem Ipsum is simply dummy text of the printing and typesetting industry. Lorem Ipsum has been the industry's standard dummy text ever since the 1500s, when an unknown printer took a galley of type and scrambled it to make a type specimen book.</p>
    <p style="margin-top:18px">It has survived not only five centuries, but also the leap into electronic typesetting, remaining essentially unchanged.</p>
    <p style="margin-top:18px">It was popularised in the 1960s with the release of Typeline sheets containing Lorem Ipsum passages, and more recently with desktop publishing software like PageForge including versions of Lorem Ipsum.</p>
  </div>
</section>

<form class="abs booking-form">
  <span class="field-label" style="left:38px;top:22px">Full name</span>
  <div class="field" style="left:38px;top:44px;width:176px"></div>
  <span class="field-label" style="left:228px;top:22px">Number of people</span>
  <div class="field" style="left:228px;top:44px;width:180px">6<svg class="caret" width="9" height="6"><path d="M0 0h9L4.5 6z" fill="#444"/></svg></div>
  <span class="field-label" style="left:38px;top:90px">Date from</span>
  <div class="field" style="left:38px;top:112px;width:176px">15.9.2018<svg class="caret" width="9" height="6"><path d="M0 0h9L4.5 6z" fill="#444"/></svg></div>
  <span class="field-label" style="left:228px;top:90px">Date To:</span>
  <div class="field" style="left:228px;top:112px;width:180px">30.9.2018<svg class="caret" width="9" height="6"><path d="M0 0h9L4.5 6z" fill="#444"/></svg></div>
  <span class="field-label" style="left:38px;top:158px">Yacht Type Interested in:</span>
  <div class="field" style="left:38px;top:180px;width:370px">Motor Yacht<svg class="caret" width="9" height="6"><path d="M0 0h9L4.5 6z" fill="#444"/></svg></div>
  <span class="field-label" style="left:38px;top:226px">Email Address</span>
  <div class="field" style="left:38px;top:248px;width:176px"></div>
  <span class="field-label" style="left:228px;top:226px">Phone Number</span>
  <div class="field" style="left:228px;top:248px;width:180px"></div>
  <span class="field-label" style="left:38px;top:296px">Massage</span>
  <div class="field" style="left:38px;top:318px;width:370px;height:118px"></div>
  <div class="btn btn-white" style="left:150px;top:460px;width:142px;height:38px">Book a Yacht!</div>
</form>

<footer class="abs site-footer"></footer>
<h4 class="footer-head" style="left:111px">ABOUT US</h4>
<div class="footer-rule" style="left:111px"></div>
<p class="footer-text" style="left:111px;top:4266px;width:190px">Lorem Ipsum is simply dummy text of the printing and typesetting industry. Lorem Ipsum has been the industry's standard dummy text.</p>
<div class="abs" style="left:111px;top:4376px;display:flex;gap:28px">
  <svg width="18" height="18"><circle cx="9" cy="9" r="8" fill="#fff"/></svg>
  <svg width="18" height="18"><circle cx="9" cy="9" r="8" fill="#fff"/></svg>
  <svg width="18" height="18"><circle cx="9" cy="9" r="8" fill="#fff"/></svg>
  <svg width="18" height="18"><circle cx="9" cy="9" r="8" fill="#fff"/></svg>
</div>

<h4 class="footer-head" style="left:374px">NEWSLETTER</h4>
<div class="footer-rule" style="left:374px"></div>
<p class="footer-text" style="left:374px;top:4266px;width:200px">Lorem Ipsum is simply dummy text of the printing .</p>
<div class="abs" style="left:374px;top:4320px;width:226px;height:34px;border-radius:17px;background:var(--white);font-size:12px;color:#444;display:flex;align-items:center;padding-left:22px">Email Address</div>
<div class="btn btn-white" style="left:374px;top:4364px;width:128px;height:34px">Subscribe</div>

<h4 class="footer-head" style="left:661px">QUICK LINKS</h4>
<div class="footer-rule" style="left:661px"></div>
<ul class="footer-list" style="left:661px"><li>Home</li><li>Charter a yacht</li><li>Locations</li><li>About us</li><li>Contact us</li></ul>

<h4 class="footer-head" style="left:883px">QUICK LINKS</h4>
<div class="footer-rule" style="left:883px"></div>
<ul class="contact-list">
  <li><svg width="14" height="14" viewBox="0 0 24 24"><path fill="#fff" d="M6.6 10.8a15 15 0 0 0 6.6 6.6l2.2-2.2c.3-.3.7-.4 1-.2 1.1.4 2.3.6 3.6.6.6 0 1 .4 1 1V20c0 .6-.4 1-1 1A17 17 0 0 1 3 4c0-.6.4-1 1-1h3.5c.6 0 1 .4 1 1 0 1.3.2 2.5.6 3.6.1.3 0 .7-.2 1z"/></svg>+012-555-0142</li>
  <li><svg width="14" height="14" viewBox="0 0 24 24"><path fill="#fff" d="M6.6 10.8a15 15 0 0 0 6.6 6.6l2.2-2.2c.3-.3.7-.4 1-.2 1.1.4 2.3.6 3.6.6.6 0 1 .4 1 1V20c0 .6-.4 1-1 1A17 17 0 0 1 3 4c0-.6.4-1 1-1h3.5c.6 0 1 .4 1 1 0 1.3.2 2.5.6 3.6.1.3 0 .7-.2 1z"/></svg>+012-555-0143</li>
  <li><svg width="14" height="12" viewBox="0 0 24 18"><rect x="1" y="1" width="22" height="16" fill="none" stroke="#fff" stroke-width="2"/><path d="M1 1l11 9 11-9" fill="none" stroke="#fff" stroke-width="2"/></svg>info@brellavon.com</li>
  <li style="align-items:flex-start"><svg width="14" height="16" viewBox="0 0 24 28" style="margin-top:6px"><path fill="#fff" d="M12 0a9 9 0 0 0-9 9c0 7 9 19 9 19s9-12 9-19a9 9 0 0 0-9-9zm0 12a3 3 0 1 1 0-6 3 3 0 0 1 0 6z"/></svg><span>48 Harbor Lane<br>Bayport, ME 04021</span></li>
</ul>

<div class="abs bottom-bar">
  <span class="abs" style="left:111px;top:22px">© Copyright 2018 Brellavon Yacht Charter Broker. All Right Reserved</span>
  <span class="abs" style="left:876px;top:22px">Privacy Policy - Terms &amp; Conditions</span>
</div>

</body>
</html>
```